Harmony Four Showcase
Date: Sunday Oct 2, 2022
When: 2-4 p.m.
Location: Brindle9 Alehouse
413 Marigold Wy #200, Sacramento, CA 95821
Tickets: www.Ticketwisp.example
General seating: $15 for adults and $10 for students

```html
<!DOCTYPE html>
<html lang="en">
<head>
<meta charset="utf-8">
<title>Harmony Four Showcase</title>
<link href="https://fonts.googleapis.com/css2?family=Playfair+Display:ital,wght@1,700;1,800&family=Cinzel:wght@500;600&family=Montserrat:ital,wght@0,400;1,800&family=Roboto:ital,wght@1,700&display=swap" rel="stylesheet">
<style>
  :root {
    --page-bg: #c4c4c4;
    --poster-bg: #07090d;
    --ink-white: #f4f6f8;
    --title-cyan: #4cc4ec;
    --title-blue: #3d74d6;
    --accent-cyan: #19b3d6;
    --seat-blue: #2a63c8;
    --seat-box: #142a52;
    --frame-line: #2f6fb8;
    --smoke-red: #c4261c;
    --footer-dark: #15222d;
    --footer-mid: #22313d;
    --address-ink: #e6f6fc;
    --booking-ink: #35c3ea;
  }
  * { margin: 0; padding: 0; box-sizing: border-box; }
  html, body { width: 1200px; height: 2400px; overflow: hidden; background: var(--page-bg); }
  .canvas { position: relative; width: 1200px; height: 2400px; }
  .poster {
    position: absolute; left: 60px; top: 488px; width: 1080px; height: 1424px;
    background:
      radial-gradient(ellipse 260px 360px at 0 60px, rgba(196,38,28,.55), transparent 70%),
      radial-gradient(ellipse 260px 360px at 1080px 60px, rgba(196,38,28,.5), transparent 70%),
      var(--poster-bg);
    overflow: hidden;
    box-shadow: 0 14px 30px rgba(0,0,0,.35);
  }
  .poster > * { position: absolute; }
  .title-main, .title-sub { left: 0; width: 100%; text-align: center; line-height: 1;
    font-family: "Playfair Display", Georgia, serif; font-style: italic; font-weight: 800; }
  .title-main { top: 58px; font-size: 122px; letter-spacing: -2px;
    background: linear-gradient(90deg, var(--title-cyan) 0%, var(--title-cyan) 45%, var(--title-blue) 60%, var(--title-cyan) 100%);
    -webkit-background-clip: text; background-clip: text; color: transparent; }
  .title-sub { top: 160px; font-size: 96px; color: var(--ink-white); }
  .divider { left: 168px; top: 282px; width: 744px; height: 16px; }
  .event-time { left: 0; top: 332px; width: 100%; text-align: center; line-height: 1;
    font-family: "Cinzel", serif; font-weight: 500; font-size: 54px; color: var(--ink-white); }
  .event-time .hl { color: var(--accent-cyan); }
  .stage-photo { left: 0; top: 380px; width: 1080px; height: 820px;
    background:
      radial-gradient(ellipse 540px 70px at 540px 780px, rgba(196,38,28,.75), transparent 75%),
      radial-gradient(circle 300px at 560px 330px, rgba(25,140,160,.45), transparent 80%),
      radial-gradient(ellipse 240px 320px at 560px 420px, rgba(150,60,70,.35), transparent 80%); }
  .stage-ring { left: 0; top: 380px; width: 1080px; height: 820px; }
  .seating-label { left: 303px; top: 908px; width: 460px; height: 54px; }
  .seating-label svg { position: absolute; inset: 0; }
  .seating-label span { position: relative; display: block; text-align: center; line-height: 54px;
    font-family: "Cinzel", serif; font-weight: 600; font-size: 40px; color: var(--seat-blue); }
  .price-frame { left: 200px; top: 976px; width: 680px; height: 196px; }
  .price { top: 1000px; width: 300px; text-align: center; color: var(--ink-white); }
  .price.adults { left: 241px; }
  .price.students { left: 530px; }
  .price b { display: block; font-family: "Montserrat", sans-serif; font-style: italic; font-weight: 800;
    font-size: 80px; line-height: 84px;
    background: linear-gradient(180deg, #6fd2f2, var(--title-blue)); -webkit-background-clip: text; background-clip: text; color: transparent; }
  .price small { display: block; font-family: "Montserrat", sans-serif; font-weight: 400; font-size: 42px; line-height: 46px; letter-spacing: 1px; }
  .footer { left: 0; top: 1213px; width: 1080px; height: 211px; }
  .address { left: 0; top: 1226px; width: 100%; text-align: center;
    font-family: "Roboto", sans-serif; font-style: italic; font-weight: 700; font-size: 34px; line-height: 43px; color: var(--address-ink); }
  .booking { left: 0; top: 1352px; width: 100%; text-align: center;
    font-family: "Roboto", sans-serif; font-style: italic; font-weight: 700; font-size: 27px; color: var(--booking-ink); }
</style>
</head>
<body>
<div class="canvas">
  <section class="poster">
    <div class="stage-photo" role="img" aria-label="Singer performing with a microphone in teal and red stage light"></div>
    <svg class="stage-ring" viewBox="0 0 1080 820" aria-hidden="true">
      <circle cx="540" cy="330" r="325" fill="none" stroke="#1fb0c4" stroke-width="4" opacity=".7"/>
    </svg>

    <h1 class="title-main">Harmony Four</h1>
    <div class="title-sub">Showcase</div>

    <svg class="divider" viewBox="0 0 744 16" aria-hidden="true">
      <line x1="0" y1="8" x2="320" y2="8" stroke="#2f6fb8" stroke-width="1.5"/>
      <line x1="424" y1="8" x2="744" y2="8" stroke="#2f6fb8" stroke-width="1.5"/>
      <ellipse cx="372" cy="8" rx="44" ry="7" fill="none" stroke="#3a8fd8" stroke-width="2"/>
    </svg>

    <div class="event-time">2-4 p.m. Sunday <span class="hl">Oct 2</span>, 2022</div>

    <div class="seating-label">
      <svg viewBox="0 0 460 54" preserveAspectRatio="none" aria-hidden="true">
        <polygon points="14,0 446,0 460,27 446,54 14,54 0,27" fill="var(--seat-box)"/>
      </svg>
      <span>General Seating:</span>
    </div>

    <svg class="price-frame" viewBox="0 0 680 196" aria-hidden="true">
      <g fill="none" stroke="var(--frame-line)" stroke-width="2">
        <polyline points="70,6 610,6 676,98 610,190 70,190 4,98 70,6"/>
        <line x1="260" y1="14" x2="420" y2="14" stroke-width="1"/>
        <line x1="260" y1="182" x2="420" y2="182" stroke-width="1"/>
        <line x1="321" y1="30" x2="321" y2="170"/>
      </g>
    </svg>

    <div class="price adults"><b>$15</b><small>for adults</small></div>
    <div class="price students"><b>$10</b><small>for students</small></div>

    <svg class="footer" viewBox="0 0 1080 211" aria-hidden="true">
      <rect x="0" y="0" width="1080" height="110" fill="var(--accent-cyan)"/>
      <rect x="0" y="110" width="1080" height="101" fill="var(--footer-dark)"/>
      <polygon points="20,30 110,30 210,110 0,110 0,60" fill="var(--footer-mid)"/>
      <polygon points="1060,30 970,30 870,110 1080,110 1080,60" fill="var(--footer-mid)"/>
    </svg>

    <p class="address">Brindle9 Alehouse 413 Marigold Wy #200,<br>Sacramento, CA 95821</p>
    <p class="booking">For booking visit the website: www.Ticketwisp.example</p>
  </section>
</div>
</body>
</html>
```